브랜드 소개
모렐빈은 “Handmade Premium”이라는 슬로건 아래 음료 비지니스 전반에 걸친 사업을 활발하게 전개중인 콜드브루 전문 제조 기업입니다.
이번 신규 콜드브루 티 (RTD) 출시를 기점으로 실행되는 패키지 디자인 공모전을 통해 더욱 다양한 소비자들에게 콜드브루 음료에 대한 이해를 넓히는 동시에 앞으로 더욱 다양한 콜드브루 음료들을 소개하고자 합니다.
모렐빈 RTD음료 (400mL) 패키지 디자인 공모전

```html
<!DOCTYPE html>
<html lang="ko">
<head>
<meta charset="utf-8">
<title>MORELVIN Flower Cold Brew Tea Labels</title>
<link rel="stylesheet" href="https://fonts.googleapis.com/css2?family=Montserrat:wght@400;500;600;700;800&family=Noto+Sans+KR:wght@500;700&display=swap">
<style>
  :root {
    --bg: #f1f0ee;
    --pink-label: #ef7f9a;
    --pink-art-a: #e85a6e;
    --pink-art-b: #f5a3b4;
    --pink-art-c: #e0903a;
    --pink-art-d: #3d6b4a;
    --red-label: #e5354b;
    --red-art-a: #f39ab0;
    --red-art-b: #4a2d5e;
    --red-art-c: #c22a3c;
    --red-art-d: #2f5a40;
    --ink: #ffffff;
    --margin: 78px;
  }
  * { margin: 0; padding: 0; box-sizing: border-box; }
  html, body { width: 1200px; height: 1200px; overflow: hidden; }
  body {
    background: var(--bg);
    display: flex;
    align-items: center;
    justify-content: center;
    gap: 120px;
    font-family: "Montserrat", sans-serif;
    color: var(--ink);
  }
  .label {
    position: relative;
    width: 380px;
    height: 1080px;
    overflow: hidden;
  }
  .label--pink { background: var(--pink-label); }
  .label--red { background: var(--red-label); }

  .brand, .product-kr, .product-name, .rule, .flavor, .volume {
    position: absolute;
    left: var(--margin);
    text-align: left;
  }
  .brand { top: 76px; }
  .brand__name {
    font-weight: 700;
    font-size: 15px;
    letter-spacing: 0.5px;
    line-height: 1;
  }
  .brand__tagline {
    font-size: 7px;
    font-weight: 500;
    margin-top: 3px;
    opacity: 0.9;
  }
  .product-kr {
    top: 168px;
    font-family: "Noto Sans KR", sans-serif;
    font-weight: 700;
    font-size: 24px;
    letter-spacing: 0.5px;
    white-space: nowrap;
  }
  .product-name {
    top: 204px;
    font-weight: 700;
    font-size: 96px;
    letter-spacing: 3px;
    line-height: 1.1;
    white-space: nowrap;
  }
  .rule {
    top: 366px;
    width: 32px;
    height: 3px;
    background: var(--ink);
  }
  .flavor {
    top: 388px;
    font-weight: 500;
    font-size: 18px;
    letter-spacing: 1.5px;
    line-height: 1.6;
  }
  .illustration {
    position: absolute;
    left: 0; right: 0; bottom: 0;
    height: 600px;
  }
  .illustration--pink {
    background: linear-gradient(170deg, var(--pink-art-a) 0%, var(--pink-art-b) 40%, var(--pink-art-d) 62%, var(--pink-art-c) 100%);
  }
  .illustration--red {
    background: linear-gradient(170deg, var(--red-art-a) 0%, var(--red-art-c) 45%, var(--red-art-d) 65%, var(--red-art-b) 100%);
  }
  .volume {
    bottom: 128px;
    font-size: 18px;
    font-weight: 500;
    letter-spacing: 1px;
  }
</style>
</head>
<body>
  <section class="label label--pink">
    <div class="illustration illustration--pink" role="img" aria-label="Illustration of hibiscus flowers, leaves and a halved calamansi fruit on pink and orange shapes"></div>
    <div class="brand">
      <div class="brand__name">MORELVIN</div>
      <div class="brand__tagline">cold brew specialist</div>
    </div>
    <p class="product-kr">플라워 콜드브루 티</p>
    <h2 class="product-name">PINK</h2>
    <div class="rule"></div>
    <p class="flavor">CALAMANSI<br>HIBISCUS</p>
    <p class="volume">400mL</p>
  </section>

  <section class="label label--red">
    <div class="illustration illustration--red" role="img" aria-label="Illustration of hibiscus flowers, leaves and a strawberry on pink and purple shapes"></div>
    <div class="brand">
      <div class="brand__name">MORELVIN</div>
      <div class="brand__tagline">cold brew specialist</div>
    </div>
    <p class="product-kr">플라워 콜드브루 티</p>
    <h2 class="product-name">RED</h2>
    <div class="rule"></div>
    <p class="flavor">STRAWBERRY<br>HIBISCUS</p>
    <p class="volume">400mL</p>
  </section>
</body>
</html>
```